We are looking to improve our packaging, because we are wanting to secure our products into five star hotels, spa and wellness centres and maybe even high end retail department stores. That is why it is important it must look the part. We are even prepared to change our current packaging (White stand up pouches) for something different e.g box etc...

Please keep in mind when designing our new Serenwell packaging that our product range will extend to Room Sprays, Candles, Diffuser, Essential Oils, Soaps, Body Scrubs, Milk Baths, Body Lotions, Face Products. So the design will need to compliment and we must be able to adjust the artwork with ease to fit bottles big and small, tubes, boxes glass jars etc... at later stage.

Please see inspiration images of packaging I like. But please do not copy them. We would like something that is unique to our brand that will last for 2-4 years before we have to change the packaging again.

Our current packaging is in a white stand up pouches.
Updates

Project Deadline Extended Reason: Hi All,I have decided to extend the Serenwell Calm Mix Packaging project as the designs I have received are not what I am looking for and are not polished enough for the retail health and spa market. Some of the ideas I received are on the right track, but they need to be reworked a bit more to give our packaging a premium high end looking product. I am trying to get our products into large retail outlets department stores, Chemists, Health and natural product stores, 5 star spa resorts and hotels and eventually export it globally and with so many similar products available for sale our products needs to stand out from the rest of the competition. We use premium grade salts with natural and organic ingredients in our products when we make them. They do not have any harsh chemicals in them. At the moment I am keeping to the stand up white pouches for now, but this will change later this year to a box. We have a good product that sells well, but our current look and feel of our packaging is letting us down and making it difficult to market into the bigger retail stores. I have attached a few sample ideas of what we like, but with our own unique mark to it. We would like something that is unique to us to give our Serenwell brand its own identity. I will leave this up to your creative skills.Our Serenwell product range will branch out to the following in a couple of months. Body Scrubs, Liquid Soaps, Soaps, Body and Face Lotions, Milk baths, Bath and Spa Tea Bags, Bubble Paths, Herbal and Fragranced Bath & Spa products, Steam Therapy, Massage and Bath Oils, Room Sprays, Home Fragrances and Essential oils. So please keep this mind when designing a label that it must be easily adapted to different shapes and size products. e.g. boxes, jars, tubes and bottles.If you have any question before you start, please send me a message.Thank you for taking the time to read our extended brief and very excited to see your designs. Kind Regards, Added Saturday, January 9, 2016

Target Market(s)

Male and female, natural products, well-being, holistic, wellness centres, spa resorts, 5 stars hotels and upmarket.

Industry/Entity Type

Health And Wellness

Font styles to use
Serif
Sans Serif
Other font styles liked:
• Open Sans

Requirements
Must have
• Front: Company Name: Brand name Serenwell Calm Mix (See logo attached or feel fry to add your design flair to this). Please insert Front Packaging copy, 100% pure & natural logo, weight of item 1kg
• Back: Palvex logo (attached), Australian Packed & Owned logo (attached or you can just use type), Please use Back Packaging copy attached. Please allow space for barcode, Batch number and expiry date.
Nice to have
• Vector background, natural earthy feel, natural or organic textures
• but we are open to any suggestions you might have.

```html
<!DOCTYPE html>
<html lang="en">
<head>
<meta charset="utf-8">
<title>Serenwell Calm Mix – Pouch Front</title>
<link rel="stylesheet" href="https://fonts.googleapis.com/css2?family=Open+Sans:wght@600;700&family=Marcellus&family=Gilda+Display&display=swap">
<style>
  :root {
    --stage: #d4d4d4;
    --pouch: #ffffff;
    --ink: #111111;
    --plum-deep: #2a0012;
    --plum: #7a0a4c;
    --plum-light: #e9c6dc;
    --wash-pink: #f2b8dc;
    --wash-yellow: #f8e59a;
    --label-ink: #3a0a1c;
  }
  * { margin: 0; padding: 0; box-sizing: border-box; }
  html, body { width: 1200px; height: 1200px; overflow: hidden; }
  body {
    background: var(--stage);
    position: relative;
    font-family: "Gilda Display", serif;
  }
  .pouch-front {
    position: absolute;
    left: 230px; top: 40px;
    width: 740px; height: 1120px;
    background: var(--pouch);
    overflow: hidden;
  }
  .purity-claim {
    position: absolute;
    left: 60px; top: 205px;
    width: 180px;
    text-align: center;
    color: var(--label-ink);
    font-family: "Marcellus", serif;
    line-height: 1;
  }
  .purity-claim .percent { font-size: 74px; letter-spacing: -2px; }
  .purity-claim .words { font-size: 29px; margin-top: 6px; line-height: 1.02; }

  .hero-orb {
    position: absolute;
    left: 238px; top: 198px;
    width: 344px; height: 344px;
    border-radius: 50%;
    background: radial-gradient(circle at 45% 110%, var(--plum-light) 0%, var(--plum) 32%, #4a0030 62%, var(--plum-deep) 100%);
  }
  .brand-mark {
    position: absolute;
    left: 418px; top: 292px;
    display: flex; align-items: center; gap: 8px;
    color: #ffffff;
    font-family: "Open Sans", sans-serif;
    font-weight: 600;
    font-size: 18px;
    line-height: 1;
    white-space: nowrap;
  }
  .brand-mark .dot {
    width: 13px; height: 13px; border-radius: 50%;
    border: 2px solid #ffffff;
    flex: none;
  }
  .watercolour-wash {
    position: absolute;
    left: 60px; top: 470px;
    width: 580px; height: 330px;
    background:
      radial-gradient(ellipse 45% 28% at 45% 70%, rgba(248,229,154,0.75), rgba(248,229,154,0) 70%),
      radial-gradient(ellipse 60% 30% at 40% 32%, rgba(242,184,220,0.75), rgba(242,184,220,0) 72%),
      radial-gradient(ellipse 20% 22% at 88% 40%, rgba(242,184,220,0.6), rgba(242,184,220,0) 72%);
  }
  .product-title {
    position: absolute;
    left: 0; right: 0; top: 522px;
    text-align: center;
    font-family: "Open Sans", sans-serif;
    color: var(--ink);
  }
  .product-title .name {
    font-weight: 700; font-size: 64px; letter-spacing: 1px; line-height: 1;
  }
  .product-title .range {
    font-weight: 600; font-size: 33px; margin-top: 8px; line-height: 1;
  }
  .product-copy {
    position: absolute;
    left: 0; right: 0; top: 845px;
    text-align: center;
    font-size: 22px;
    line-height: 28px;
    color: var(--ink);
  }
  .net-weight {
    position: absolute;
    left: 0; right: 0; top: 1040px;
    text-align: center;
    font-size: 38px;
    color: var(--ink);
  }
</style>
</head>
<body>
  <main class="pouch-front">
    <div class="watercolour-wash" role="img" aria-label="Soft pink and yellow watercolour wash behind the product name"></div>

    <div class="purity-claim">
      <div class="percent">100%</div>
      <div class="words">PURE &amp;<br>NATURAL</div>
    </div>

    <div class="hero-orb" role="img" aria-label="Deep plum circle with flowing white line artwork"></div>

    <div class="brand-mark">
      <span class="dot"></span>
      <span>Serenwell</span>
    </div>

    <h1 class="product-title">
      <div class="name">SERENWELL</div>
      <div class="range">CALM MIX</div>
    </h1>

    <p class="product-copy">
      A unique blend of himalayan rock salt<br>
      and magnesium flakes<br>
      for the ultimate therapeutic bath soak.<br>
      Our Serenwell Calm Mix will detoxify<br>
      and revitalise your body.
    </p>

    <div class="net-weight">1kg</div>
  </main>
</body>
</html>
```